Young Entrepreneur needs the sexiest, slickest, hottest ANDROID ALARM APP DESIGN.

Now that I have your attention...

The name of the Application is PlumDrift, using 'Stickers' this application is meant to get you to do what you need to do AND TO DO IT NOW, with a UI so simple my grandma can use it.

Using the provided sketches as a REFERENCE point, THREE (3) SCREENS will be needed, including a couple of design accents, which when the project is completed will be sent directly to a programming team.

Industry/Entity Type

Android

Requirements
Must have
• Creativity in simplicity. but please, go wild, do your 'thang'... Just keep it simple and clean.

```html
<!DOCTYPE html>
<html lang="en">
<head>
<meta charset="utf-8">
<title>PlumDrift – Alarm App Screens</title>
<link href="https://fonts.googleapis.com/css2?family=Quicksand:wght@400;500;700&display=swap" rel="stylesheet">
<style>
  :root {
    --page: #ffffff;
    --screen: #454545;
    --cyan: #3fe3ea;
    --white: #ffffff;
    --muted: #b8b8b8;
    --rule: #9a9a9a;
    --tick: #4ee64a;
  }
  * { box-sizing: border-box; margin: 0; padding: 0; }
  html, body { width: 1200px; height: 900px; overflow: hidden; background: var(--page); }
  body { position: relative; font-family: "Quicksand", sans-serif; color: var(--white); }

  .screen { position: absolute; top: 232px; height: 431px; background: var(--screen); }
  .screen--alarm { left: 40px; width: 241px; }
  .screen--list { left: 322px; width: 260px; }
  .screen--detail { left: 613px; width: 262px; }
  .screen--days { left: 898px; width: 262px; }

  .brand { position: absolute; top: 24px; left: 0; right: 0; text-align: center;
           font-weight: 700; font-size: 30px; color: var(--cyan); }
  .brand-small { position: absolute; top: 14px; right: 16px; font-weight: 700; font-size: 17px; color: var(--cyan); }
  .back { position: absolute; top: 10px; left: 14px; font-size: 26px; line-height: 1; color: var(--white); }

  .note { position: absolute; }
  .note svg { position: absolute; inset: 0; width: 100%; height: 100%; overflow: visible; }
  .note-body { fill: none; stroke: var(--white); stroke-width: 2; vector-effect: non-scaling-stroke; }
  .note-content { position: relative; text-align: center; }

  .alarm-note { left: 31px; top: 115px; width: 162px; height: 158px; }
  .alarm-note .note-content { padding-top: 10px; }
  .alarm-time { font-size: 48px; color: var(--cyan); line-height: 1; font-weight: 400; }
  .alarm-ampm { font-size: 22px; color: var(--cyan); line-height: 1.1; }
  .alarm-label { font-size: 31px; line-height: 1.2; }
  .alarm-date { position: absolute; top: 291px; left: 0; right: 0; text-align: center; color: var(--cyan); font-size: 19px; }
  .screen-actions { position: absolute; bottom: 14px; left: 34px; right: 28px; display: flex; justify-content: space-between; color: var(--muted); font-size: 15px; }

  .day-filter { position: absolute; top: 86px; left: 0; right: 0; text-align: center; font-size: 13px; color: var(--muted); letter-spacing: -0.3px; }
  .day-filter .is-active { color: var(--white); }
  .task-grid { position: absolute; top: 127px; left: 13px; display: grid; grid-template-columns: repeat(3, 72px); gap: 8px 11px; }
  .task-grid .note { position: relative; width: 72px; height: 70px; }
  .task-grid .note-content { padding-top: 14px; }
  .task-time { color: var(--cyan); font-size: 15px; line-height: 1; }
  .task-time small { font-size: 10px; }
  .task-label { font-size: 19px; line-height: 1.2; }
  .add-note { left: 13px; top: 282px; width: 72px; height: 72px; }
  .add-button { position: absolute; left: 14px; top: 14px; width: 42px; height: 42px; background: var(--cyan); border-radius: 3px; }
  .add-button svg { width: 100%; height: 100%; }

  .rule { position: absolute; left: 10px; right: 10px; height: 2px; background: var(--rule); }
  .detail-time { position: absolute; top: 66px; left: 0; right: 0; text-align: center; color: var(--cyan); font-size: 44px; line-height: 1; }
  .detail-time small { font-size: 22px; }
  .detail-label { position: absolute; top: 108px; left: 0; right: 0; text-align: center; font-size: 33px; line-height: 1; }
  .option { position: absolute; left: 50%; transform: translateX(-50%); height: 30px; padding: 0 4px 0 10px;
            border: 2px solid var(--white); border-radius: 15px; display: flex; align-items: center; gap: 6px;
            color: var(--cyan); font-size: 17px; white-space: nowrap; }
  .option .off { color: var(--muted); }
  .option-icon { width: 22px; height: 22px; border-radius: 50%; background: var(--white); display: flex; align-items: center; justify-content: center; }
  .option-icon svg { width: 16px; height: 16px; }

  .header-title { position: absolute; top: 18px; left: 38px; font-size: 16px; }
  .summary { position: absolute; top: 65px; left: 28px; right: 20px; display: flex; justify-content: space-between; font-size: 22px; }
  .summary-time { color: var(--cyan); }
  .day-list { position: absolute; top: 119px; left: 32px; list-style: none; }
  .day-list li { display: flex; align-items: center; gap: 10px; height: 32px; font-size: 19px; }
  .checkbox { width: 18px; height: 18px; border: 2px solid var(--white); position: relative; }
  .checkbox svg { position: absolute; left: -1px; top: -9px; width: 22px; height: 22px; }
</style>
</head>
<body>

<section class="screen screen--alarm">
  <div class="brand">PlumDrift</div>
  <div class="note alarm-note">
    <svg viewBox="0 0 100 100" preserveAspectRatio="none" aria-hidden="true">
      <path class="note-body" d="M12 0H88Q100 0 100 12V76L76 100H12Q0 100 0 88V12Q0 0 12 0Z"/>
      <path class="note-body" d="M76 100Q78 80 100 76"/>
    </svg>
    <div class="note-content">
      <div class="alarm-time">06:50</div>
      <div class="alarm-ampm">am</div>
      <div class="alarm-label">Shower</div>
    </div>
  </div>
  <div class="alarm-date">Tue, Dec 30 2013</div>
  <div class="screen-actions"><span>CLOSE</span><span>EDIT</span></div>
</section>

<section class="screen screen--list">
  <div class="brand">PlumDrift</div>
  <div class="day-filter"><span class="is-active">ALL</span>&nbsp; MON TUE WED THU FRI SAT SUN</div>
  <div class="task-grid">
    <div class="note"><svg viewBox="0 0 100 100" preserveAspectRatio="none" aria-hidden="true"><path class="note-body" d="M12 0H88Q100 0 100 12V78L78 100H12Q0 100 0 88V12Q0 0 12 0Z"/><path class="note-body" d="M78 100Q80 82 100 78"/></svg>
      <div class="note-content"><div class="task-time">04:30<small>am</small></div><div class="task-label">Shower</div></div></div>
    <div class="note"><svg viewBox="0 0 100 100" preserveAspectRatio="none" aria-hidden="true"><path class="note-body" d="M12 0H88Q100 0 100 12V78L78 100H12Q0 100 0 88V12Q0 0 12 0Z"/><path class="note-body" d="M78 100Q80 82 100 78"/></svg>
      <div class="note-content"><div class="task-time">06:50<small>am</small></div><div class="task-label">Shower</div></div></div>
    <div class="note"><svg viewBox="0 0 100 100" preserveAspectRatio="none" aria-hidden="true"><path class="note-body" d="M12 0H88Q100 0 100 12V78L78 100H12Q0 100 0 88V12Q0 0 12 0Z"/><path class="note-body" d="M78 100Q80 82 100 78"/></svg>
      <div class="note-content"><div class="task-time">08:00<small>am</small></div><div class="task-label">Shower</div></div></div>
    <div class="note"><svg viewBox="0 0 100 100" preserveAspectRatio="none" aria-hidden="true"><path class="note-body" d="M12 0H88Q100 0 100 12V78L78 100H12Q0 100 0 88V12Q0 0 12 0Z"/><path class="note-body" d="M78 100Q80 82 100 78"/></svg>
      <div class="note-content"><div class="task-time">01:30<small>pm</small></div><div class="task-label">Shower</div></div></div>
    <div class="note"><svg viewBox="0 0 100 100" preserveAspectRatio="none" aria-hidden="true"><path class="note-body" d="M12 0H88Q100 0 100 12V78L78 100H12Q0 100 0 88V12Q0 0 12 0Z"/><path class="note-body" d="M78 100Q80 82 100 78"/></svg>
      <div class="note-content"><div class="task-time">05:25<small>pm</small></div><div class="task-label">Shower</div></div></div>
    <div class="note"><svg viewBox="0 0 100 100" preserveAspectRatio="none" aria-hidden="true"><path class="note-body" d="M12 0H88Q100 0 100 12V78L78 100H12Q0 100 0 88V12Q0 0 12 0Z"/><path class="note-body" d="M78 100Q80 82 100 78"/></svg>
      <div class="note-content"><div class="task-time">08:50<small>pm</small></div><div class="task-label">Shower</div></div></div>
  </div>
  <div class="note add-note">
    <svg viewBox="0 0 100 100" preserveAspectRatio="none" aria-hidden="true"><path class="note-body" d="M12 0H88Q100 0 100 12V78L78 100H12Q0 100 0 88V12Q0 0 12 0Z"/><path class="note-body" d="M78 100Q80 82 100 78"/></svg>
    <div class="add-button"><svg viewBox="0 0 42 42" aria-label="Add task"><path d="M21 8V34M8 21H34" stroke="#454545" stroke-width="3"/></svg></div>
  </div>
</section>

<section class="screen screen--detail">
  <div class="back">‹</div>
  <div class="brand-small">PlumDrift</div>
  <div class="rule" style="top:57px"></div>
  <div class="detail-time">06:50<small>am</small></div>
  <div class="detail-label">Shower</div>
  <div class="rule" style="top:151px"></div>
  <div class="option" style="top:175px">ON/<span class="off">OFF</span>
    <span class="option-icon"><svg viewBox="0 0 16 16"><circle cx="8" cy="8" r="6" fill="none" stroke="#454545" stroke-width="1.6"/><path d="M8 2V8" stroke="#454545" stroke-width="1.6"/></svg></span></div>
  <div class="option" style="top:214px">SET STICKY
    <span class="option-icon"><svg viewBox="0 0 16 16"><circle cx="8" cy="6" r="4" fill="#454545"/><path d="M8 9V15" stroke="#454545" stroke-width="1.6"/></svg></span></div>
  <div class="option" style="top:253px">SOUND
    <span class="option-icon"><svg viewBox="0 0 16 16"><path d="M3 6H6L10 3V13L6 10H3Z" fill="#454545"/></svg></span></div>
  <div class="option" style="top:292px">COLOR
    <span class="option-icon"><svg viewBox="0 0 16 16"><path d="M8 8L8 1A7 7 0 0 1 15 8Z" fill="#e33"/><path d="M8 8L15 8A7 7 0 0 1 8 15Z" fill="#fc3"/><path d="M8 8L8 15A7 7 0 0 1 1 8Z" fill="#3c6"/><path d="M8 8L1 8A7 7 0 0 1 8 1Z" fill="#39f"/></svg></span></div>
  <div class="option" style="top:349px">DELETE
    <span class="option-icon"><svg viewBox="0 0 16 16"><circle cx="8" cy="8" r="6.5" fill="none" stroke="#454545" stroke-width="1.3"/><path d="M5 5L11 11M11 5L5 11" stroke="#454545" stroke-width="1.6"/></svg></span></div>
  <div class="option" style="top:388px">SAVE
    <span class="option-icon"><svg viewBox="0 0 16 16"><rect x="3" y="3" width="10" height="10" fill="none" stroke="#454545" stroke-width="1.4"/><path d="M5 5L11 11M11 7V11H7" fill="none" stroke="#454545" stroke-width="1.4"/></svg></span></div>
</section>

<section class="screen screen--days">
  <div class="back">‹</div>
  <div class="header-title">SET STICKY</div>
  <div class="brand-small">PlumDrift</div>
  <div class="rule" style="top:57px"></div>
  <div class="summary"><span class="summary-time">06:50am</span><span>Shower</span></div>
  <div class="rule" style="top:100px"></div>
  <ul class="day-list">
    <li><span class="checkbox"></span>All Days</li>
    <li><span class="checkbox"><svg viewBox="0 0 22 22"><path d="M3 12L9 18L20 3" fill="none" stroke="var(--tick)" stroke-width="3.5"/></svg></span>Monday</li>
    <li><span class="checkbox"><svg viewBox="0 0 22 22"><path d="M3 12L9 18L20 3" fill="none" stroke="var(--tick)" stroke-width="3.5"/></svg></span>Tuesday</li>
    <li><span class="checkbox"><svg viewBox="0 0 22 22"><path d="M3 12L9 18L20 3" fill="none" stroke="var(--tick)" stroke-width="3.5"/></svg></span>Wednesday</li>
    <li><span class="checkbox"></span>Thursday</li>
    <li><span class="checkbox"><svg viewBox="0 0 22 22"><path d="M3 12L9 18L20 3" fill="none" stroke="var(--tick)" stroke-width="3.5"/></svg></span>Friday</li>
    <li><span class="checkbox"><svg viewBox="0 0 22 22"><path d="M3 12L9 18L20 3" fill="none" stroke="var(--tick)" stroke-width="3.5"/></svg></span>Saturday</li>
    <li><span class="checkbox"></span>Sunday</li>
  </ul>
</section>

</body>
</html>
```